Mobile Recording Studio needs business cards

Open to seeing a creative design, but I want to emphasis my logo and minimize the name/title and company information. Possible a fully black background on card.

My company is a mobile sound recording studio. ok to include a my trailer (actual or cartoon) on the card. My initial thought is more straight forward, but a good design will win me over.

SPECS:
CMYK color mode
High (300ppi) raster effect.
cover bleed area
please deliver: Illustrator file with layers and a pdf at completion.

Name and info for the business card:

Dallin Perry
ADR Mixer

email: Dallin@MixVault.com

address:
248 - 5170 East Hollister
Vancouver, BC V5R 2J4

phone:
604.518.2093 office

website:
www.MixVault.com

FB: @MixVault

Instagram: @TheMixVault

Industry/Entity Type

Television Production

Contact Information for Business Card

Dallin Perry
ADR Mixer

email: Dallin@MixVault.com

address:
248 - 5170 East Hollister
Vancouver, BC V5R 2J4

phone:
604.518.2093 office

website:
www.MixVault.com

FB: @MixVault

Instagram: @TheMixVault

Colors

Designer to choose colors to be used in the design.

Requirements
Must have
• emphasis my logo and minimize the name/title and company information.
• SPECS:
• CMYK color mode
• High (300ppi) raster effect.
• cover bleed area
• please deliver: Illustrator file with layers and a pdf at completion.
Nice to have
• maybe include the following:
• all black background or black theme
• my work trailer (actual or cartoon) refer to Instagram: @TheMixVault

```html
<!DOCTYPE html>
<html lang="en">
<head>
<meta charset="utf-8">
<title>MixVault Business Cards</title>
<link href="https://fonts.googleapis.com/css2?family=Poppins:wght@300;400;700&display=swap" rel="stylesheet">
<style>
  :root {
    --page-bg: #1b1b1d;
    --card-dark: #0d0d0e;
    --card-mid: #1c1c1e;
    --silver: #d4d4d6;
    --silver-soft: #b9b9bc;
    --grey-name: #a9a9ac;
    --divider: #8a8a8d;
  }
  * { margin: 0; padding: 0; box-sizing: border-box; }
  html, body {
    width: 1200px; height: 960px; overflow: hidden;
    background: var(--page-bg);
    font-family: "Poppins", sans-serif;
  }
  .canvas {
    width: 1200px; height: 960px;
    display: flex; flex-direction: column;
    align-items: center; justify-content: center; gap: 30px;
  }
  .card {
    position: relative;
    width: 760px; height: 434px;
    background:
      repeating-linear-gradient(90deg, rgba(255,255,255,0.018) 0 1px, transparent 1px 3px),
      linear-gradient(160deg, var(--card-mid) 0%, var(--card-dark) 55%, #080809 100%);
    box-shadow: 0 10px 30px rgba(0,0,0,0.55);
    overflow: hidden;
  }
  /* Front */
  .card-front { display: flex; align-items: center; justify-content: center; }
  .brand { display: flex; align-items: center; gap: 20px; }
  .brand-mark {
    width: 26px; height: 26px; border-radius: 50%;
    background: var(--silver);
  }
  .brand-name {
    font-weight: 700; font-size: 76px; letter-spacing: 1px;
    color: var(--silver);
  }
  /* Back */
  .identity {
    position: absolute; left: 120px; top: 222px;
    text-align: right;
  }
  .person-name {
    font-weight: 700; font-size: 26px; letter-spacing: 0.5px;
    color: var(--grey-name); text-transform: uppercase; line-height: 1.1;
  }
  .person-role {
    font-weight: 300; font-size: 15px; color: var(--grey-name);
  }
  .divider {
    position: absolute; left: 408px; top: 130px;
    width: 1px; height: 150px;
    background: linear-gradient(180deg, transparent, var(--divider) 20%, var(--divider) 80%, transparent);
  }
  .contact {
    position: absolute; left: 432px; top: 118px;
    color: var(--silver); font-weight: 300; font-size: 16px; line-height: 1.45;
  }
  .contact-address { margin-bottom: 12px; }
  .contact-list { list-style: none; }
  .contact-list li { display: flex; align-items: center; gap: 10px; }
  .contact-icon { width: 12px; height: 12px; flex: none; fill: var(--silver); }
</style>
</head>
<body>
<main class="canvas">
  <section class="card card-front">
    <div class="brand">
      <span class="brand-mark"></span>
      <span class="brand-name">MixVault</span>
    </div>
  </section>

  <section class="card card-back">
    <div class="identity">
      <p class="person-name">Dallin Perry</p>
      <p class="person-role">ADR Mixer</p>
    </div>
    <div class="divider"></div>
    <div class="contact">
      <p class="contact-address">248 - 5170 East Hollister<br>Vancouver, BC V5R 2J4</p>
      <ul class="contact-list">
        <li>
          <svg class="contact-icon" viewBox="0 0 12 12"><path d="M2.4 0.8l1.8 0 0.8 2.6-1.2 1a6.5 6.5 0 0 0 3.6 3.6l1-1.2 2.6 0.8 0 1.8c0 0.6-0.5 1.1-1.1 1.1A9.9 9.9 0 0 1 1.3 1.9c0-0.6 0.5-1.1 1.1-1.1z"/></svg>
          <span>604.518.2093</span>
        </li>
        <li>
          <svg class="contact-icon" viewBox="0 0 12 12"><path d="M0.5 2.5h11v7h-11z M0.5 2.5l5.5 4 5.5-4" fill="none" stroke="#d4d4d6" stroke-width="1.2"/></svg>
          <span>Dallin@MixVault.com</span>
        </li>
        <li>
          <svg class="contact-icon" viewBox="0 0 12 12"><circle cx="6" cy="6" r="5.5"/></svg>
          <span>@TheMixVault</span>
        </li>
        <li>
          <svg class="contact-icon" viewBox="0 0 12 12"><rect x="0.5" y="0.5" width="11" height="11" rx="2"/></svg>
          <span>@TheMixVault</span>
        </li>
      </ul>
    </div>
  </section>
</main>
</body>
</html>
```